Brindle Offers is an online marketing platform.

A daily deals site for consumers a way to bring in new clients for clients and this is who the business cards are for. Industries - Food and Drink, Things To Do, Beauty and Spas, Staycations and Services.
Logo on one side.
Name - Owen Radley
Job Title - Sales Director
Phone Number - 07912358046
Email - owen@brindleoffers.co.uk
need same for second person
Name - Fiona Bracken
Job Title - Operations Director
Phone Number - 01632840275
Email - fiona@brindleoffers.co.uk
Bottom Right - Chatterbook Icon, Snapa Icon, Pipline Icon
Target Market(s)
Business owners of the above industries
Contact Information for Business Card
Name - Owen Radley
Name - Fiona Bracken
Look and feel

```html
<!DOCTYPE html>
<html lang="en">
<head>
<meta charset="utf-8">
<title>Brindle Offers – Business Card</title>
<link href="https://fonts.googleapis.com/css2?family=Roboto:wght@400;500;700&display=swap" rel="stylesheet">
<style>
  :root {
    --backdrop: #2f2f2f;
    --card-white: #ffffff;
    --brand-blue: #0a52a3;
    --ring-grey: #4a4a4c;
    --card-dark: #3a3a3b;
    --text-light: #ffffff;
  }
  html, body {
    margin: 0;
    width: 1200px;
    height: 800px;
    overflow: hidden;
    background: var(--backdrop);
    font-family: "Roboto", Arial, sans-serif;
  }
  .canvas {
    position: relative;
    width: 1200px;
    height: 800px;
  }
  .card {
    position: absolute;
    top: 120px;
    width: 340px;
    height: 560px;
    border-radius: 22px;
    overflow: hidden;
  }
  .card--front { left: 220px; background: var(--brand-blue); }
  .card--back  { left: 640px; background: var(--card-dark); }
  .card svg { display: block; }

  .front-art { position: absolute; inset: 0; }

  .brand-name {
    position: absolute;
    left: 0; right: 0;
    top: 185px;
    display: flex;
    align-items: center;
    justify-content: center;
    gap: 10px;
    color: var(--brand-blue);
    font-weight: 700;
    font-size: 30px;
    letter-spacing: 0.5px;
  }
  .brand-dot {
    width: 16px; height: 16px;
    border-radius: 50%;
    background: var(--brand-blue);
  }

  .contact {
    position: absolute;
    left: 0; right: 0;
    top: 402px;
    text-align: center;
    color: var(--text-light);
  }
  .contact__name  { font-size: 22px; font-weight: 700; margin: 0; }
  .contact__role  { font-size: 15px; font-weight: 500; margin: 2px 0 18px; }
  .contact__line  { font-size: 14px; margin: 2px 0; }
  .social {
    margin-top: 14px;
    font-size: 11px;
    font-weight: 500;
    letter-spacing: 0.3px;
  }

  .back-brand {
    position: absolute;
    inset: 0;
    display: flex;
    align-items: center;
    justify-content: center;
    gap: 12px;
    color: var(--text-light);
    font-weight: 700;
    font-size: 34px;
    padding-bottom: 70px;
  }
  .back-brand .brand-dot { background: var(--text-light); width: 20px; height: 20px; }
</style>
</head>
<body>
<main class="canvas">
  <section class="card card--front" aria-label="Business card front">
    <svg class="front-art" width="340" height="560" viewBox="0 0 340 560" aria-hidden="true">
      <rect x="0" y="0" width="340" height="250" fill="var(--card-white)"/>
      <path d="M300 45 A185 185 0 0 1 95 385" fill="none" stroke="var(--ring-grey)" stroke-width="14" stroke-linecap="round"/>
      <circle cx="180" cy="200" r="178" fill="var(--card-white)"/>
    </svg>
    <div class="brand-name"><span class="brand-dot"></span>Brindle Offers</div>
    <div class="contact">
      <p class="contact__name">Owen Radley</p>
      <p class="contact__role">Sales Director</p>
      <p class="contact__line">07912358046</p>
      <p class="contact__line">owen@brindleoffers.co.uk</p>
      <p class="social">Chatterbook · Snapa · Pipline</p>
    </div>
  </section>

  <section class="card card--back" aria-label="Business card back">
    <div class="back-brand"><span class="brand-dot"></span>Brindle Offers</div>
  </section>
</main>
</body>
</html>
```